Audio Visual company needs WordPress Site re-design

We need a new, simple and sleek redesign of our website, www.brenvalegroup.com. It is crucial that it is mobile platform friendly! The company emphasis is on commercial sound and video installation.

Examples of what our company does can be found here: http://qorlinthub.com/

I am NOT looking for a storefront or an e-commerce site. I would just like an elegant site that describes our services. Perhaps incorporate a sleek showcase into the homepage of projects we have completed. Also would like an elegant menu-bar, perhaps enhance our current site menu or similar.

Here is a link to another site that exhibits the content I am looking for. Their target market is also much like mine.
http://www.maddoxvellings.com/ ........ A polished up version of this site would probably be my ideal site. It has almost EXACTLY the content I am looking for. Exclude the "Printing & signage" category. Needs nicer menus, contact page and project showcase.

Here is another example: http://www.plumcrestgalleryav.com/ ......... This site has a very nice homepage design with a good layout and feature slider. The site is simple, elegant and to the point.

Target Market(s)

Corporate/commercial business, Educational institutions

Industry/Entity Type

E-Commerce

Font styles to use
Serif
Sans Serif

Requirements
Must have
• Mobile friendly navigation
Nice to have
• HTML5 & CSS3
Should not have
• No Adobe Flash content. No store templates or e-commerce. We are a service based company not a product sales company

```html
<!DOCTYPE html>
<html lang="en">
<head>
<meta charset="utf-8">
<title>Brenvale Group – Sound &amp; Video Solutions</title>
<link rel="stylesheet" href="https://fonts.googleapis.com/css2?family=Lato:wght@300;400;700&display=swap">
<style>
:root{
  --red:#e2001a;
  --navy:#1d1a4a;
  --ink:#1a1a1a;
  --white:#ffffff;
  --grey-band:#e9e9e9;
  --footer:#ececec;
  --star:#f6c21a;
  --hero-dark:#1b1b1b;
}
*{margin:0;padding:0;box-sizing:border-box}
html,body{width:1200px;height:2601px;overflow:hidden}
body{font-family:"Lato",Arial,sans-serif;color:var(--ink);background:var(--white);position:relative}
section,header,footer{position:absolute;left:0;width:1200px}

/* hero */
.hero{top:0;height:690px;background:radial-gradient(ellipse at 30% 40%,#4a4a4a 0%,#262626 45%,#111 100%)}
.utility-nav{position:absolute;top:14px;right:99px;font-size:12px;color:var(--white);display:flex;gap:10px}
.main-nav{position:absolute;top:49px;left:99px;width:1002px;height:88px;background:var(--white);display:flex;align-items:center;justify-content:space-between;padding:0 40px 0 20px}
.brand{display:flex;align-items:center;gap:10px;font-size:28px;font-weight:700;color:var(--navy);letter-spacing:.5px}
.brand-mark{width:18px;height:18px;background:var(--red)}
.menu{display:flex;gap:32px;font-size:16px;font-weight:700;color:var(--ink)}
.menu .active{color:var(--red)}
.slider{position:absolute;top:151px;left:99px;width:1002px;height:466px;background:linear-gradient(135deg,#2a2e34 0%,#6d6f70 45%,#b9b6ad 60%,#3c3d3f 80%,#1a1a1a 100%)}
.slide-caption{position:absolute;top:237px;left:36px;width:435px;height:113px;background:rgba(0,0,0,.85);padding:18px 14px}
.slide-caption h1{font-weight:400;font-size:40px;color:var(--red);line-height:1}
.slide-caption p{font-weight:300;font-size:26px;color:var(--white);margin-top:10px}
.slide-cta{position:absolute;top:352px;left:36px;width:193px;height:54px;background:var(--navy);color:var(--white);font-size:20px;font-weight:300;display:flex;align-items:center;justify-content:center}
.dots{position:absolute;display:flex;gap:10px}
.dots i{width:11px;height:11px;border-radius:50%;background:#333}
.dots i.on{background:var(--red)}
.slider .dots{top:420px;left:460px}

/* welcome */
.welcome{top:690px;height:371px;text-align:center}
.section-title{font-weight:400;font-size:32px;letter-spacing:.5px}
.welcome .section-title{margin-top:46px}
.welcome p{width:968px;margin:28px auto 0;font-size:15.5px;line-height:27.5px}
.btn-red{display:inline-flex;align-items:center;justify-content:center;background:var(--red);color:var(--white)}
.welcome .btn-red{margin-top:42px;width:215px;height:47px;font-size:20px;font-weight:300}

/* services */
.services{top:1061px;height:552px;background:var(--grey-band)}
.services .section-title{position:absolute;top:37px;width:100%;text-align:center}
.chev{position:absolute;top:44px}
.services .grid{position:absolute;top:99px;left:111px;display:flex;gap:26px}
.card{width:309px}
.card-img{height:179px}
.card h3{font-weight:400;font-size:24px;margin-top:20px}
.card p{font-size:12.5px;line-height:20.5px;margin-top:12px;height:86px}
.card .btn-red{margin-top:26px;width:85px;height:28px;font-size:11px}

/* reviews */
.reviews{top:1613px;height:437px;background:linear-gradient(180deg,#2b2b2b 0%,#3b3b3b 50%,#1c1c1c 100%);color:var(--white)}
.reviews .section-title{position:absolute;top:40px;width:100%;text-align:center}
.reviews .grid{position:absolute;top:140px;left:111px;display:flex;gap:25px}
.review{width:310px}
.review h4{font-weight:400;font-size:16px}
.review .meta{font-size:12px;margin-top:10px}
.stars{margin-top:16px;display:block}
.review p{font-size:15px;line-height:27.5px;margin-top:10px}
.reviews .dots{top:390px;left:560px}
.reviews .dots i{background:var(--white)}
.reviews .dots i.off{background:#777}

/* news */
.news{top:2050px;height:388px}
.news .section-title{position:absolute;top:62px;left:111px}
.news-arrows{position:absolute;top:72px;left:640px}
.news .date{position:absolute;top:131px;left:111px;font-size:15px;font-weight:700;color:var(--red)}
.news h2{position:absolute;top:158px;left:111px;width:560px;font-size:24px;font-weight:700;line-height:31px}
.news .excerpt{position:absolute;top:242px;left:111px;width:560px;font-size:15px;line-height:21px}
.ad-label{position:absolute;top:35px;left:721px;font-size:10px;color:#555}
.ad-slot{position:absolute;top:55px;left:721px;width:366px;height:305px;background:linear-gradient(160deg,#e7c98c 0%,#c98e5a 40%,#6f6e73 75%,#1e1e22 100%)}

/* footer */
.site-footer{top:2438px;height:163px;background:var(--footer);text-align:center}
.social{display:flex;justify-content:center;gap:34px;margin-top:42px}
.social i{width:18px;height:18px;border-radius:50%;background:var(--navy)}
.footer-nav{margin-top:18px;font-size:16px;display:flex;justify-content:center;gap:16px}
.copyright{margin-top:14px;font-size:15px}
</style>
</head>
<body>

<header class="hero">
  <nav class="utility-nav"><span>Newsletters</span><span>|</span><span>Advertisers</span><span>|</span><span>Social Media</span></nav>
  <nav class="main-nav">
    <div class="brand"><span class="brand-mark"></span>BRENVALE GROUP</div>
    <div class="menu"><span class="active">HOME</span><span>SERVICES</span><span>CONTACT US</span><span>CUSTOMER REVIEWS</span></div>
  </nav>
  <div class="slider" role="img" aria-label="Studio microphone over a mixing console">
    <div class="slide-caption">
      <h1>BRENVALE GROUP</h1>
      <p>SOUND &amp; VIDEO SOLUTIONS</p>
    </div>
    <div class="slide-cta">LEARN MORE &gt;&gt;</div>
    <div class="dots"><i class="on"></i><i></i><i></i><i></i></div>
  </div>
</header>

<section class="welcome">
  <h2 class="section-title">WELCOME TO BRENVALE GROUP</h2>
  <p>Brenvale Group has been customizing audio and video products for home and business customers since 2007. We specialize in the design and installation of residential &amp; commercial sound systems, HD video displays, digital projection &amp; digital signage. We are located in Ashgrove Park, a northwest suburb just outside of Corvane City. Need an estimate? We will come to you! All of our estimates are done at your home or office for free. If you would prefer to come into our office, please contact us to set up an appointment. &nbsp; We believe that the customer is our number one priority.</p>
  <span class="btn-red">READ MORE</span>
</section>

<section class="services">
  <svg class="chev" style="left:110px" width="12" height="18" viewBox="0 0 12 18"><path d="M10 1 2 9l8 8" fill="none" stroke="#111" stroke-width="2"/></svg>
  <h2 class="section-title">OUR SERVICES</h2>
  <svg class="chev" style="left:1072px" width="12" height="18" viewBox="0 0 12 18"><path d="M2 1l8 8-8 8" fill="none" stroke="#111" stroke-width="2"/></svg>
  <div class="grid">
    <article class="card">
      <div class="card-img" role="img" aria-label="Person viewing a large digital display wall" style="background:linear-gradient(120deg,#0d1b3a,#2f6fc9 55%,#c33 80%,#101a33)"></div>
      <h3>Digital Media Signage</h3>
      <p>Digital signage by definition, is a form of electronic display that shows television programming, menus, information, advertising and other messages. Digital signs (frequently utilizing technologies such as LCD, LED, plasma displays, or projected images &nbsp;...</p>
      <span class="btn-red">READ MORE</span>
    </article>
    <article class="card">
      <div class="card-img" role="img" aria-label="Hand adjusting a live sound mixing desk" style="background:linear-gradient(135deg,#3a3a3a,#8a8a8a 50%,#2a2a2a)"></div>
      <h3>Live-Sound Integration</h3>
      <p>Whether it's an auditorium, gymnasium, corporate meeting room or a house of worship, Brenvale Group can design and install a state-of-the-art, custom sound system to meet your specific needs and budget. With years of experience installing ...</p>
      <span class="btn-red">READ MORE</span>
    </article>
    <article class="card">
      <div class="card-img" role="img" aria-label="Hand holding a remote control in front of a television" style="background:linear-gradient(135deg,#2b5fb8,#6a8fd4 45%,#c9a07e 70%,#2a2a2a)"></div>
      <h3>Universal Remotes</h3>
      <p>Why a universal remote control? Most of today's surround Sound Systems consist of multiple components: starting with your TV, through the surround receiver, cable/satellite box, HD disc player and perhaps Orchard TV. It can be very frustrating ...</p>
      <span class="btn-red">READ MORE</span>
    </article>
  </div>
</section>

<section class="reviews" role="img" aria-label="Home theater room with projection screen in the background">
  <h2 class="section-title">CUSTOMER REVIEWS</h2>
  <svg width="0" height="0" style="position:absolute">
    <defs>
      <polygon id="star" points="10,0 12.9,6.9 20,7.6 14.6,12.3 16.2,19.5 10,15.8 3.8,19.5 5.4,12.3 0,7.6 7.1,6.9" fill="var(--star)"/>
      <clipPath id="half"><rect x="0" y="0" width="10" height="20"/></clipPath>
    </defs>
  </svg>
  <div class="grid">
    <article class="review">
      <h4>VELTRA 525 PROJECTOR</h4>
      <div class="meta">Nov 22, 2014 by Marcus</div>
      <svg class="stars" width="160" height="22" viewBox="0 0 160 22"><use href="#star" x="0"/><use href="#star" x="32"/><use href="#star" x="64"/><use href="#star" x="96"/><polygon points="138,0 140.9,6.9 148,7.6 142.6,12.3 144.2,19.5 138,15.8 131.8,19.5 133.4,12.3 128,7.6 135.1,6.9" fill="none" stroke="var(--star)" stroke-width="1.5"/><use href="#star" x="128" clip-path="url(#half)"/></svg>
      <p>Excellent and detailed professional, with installation of interactive projector, as well customizing install on white board. I highly recommend Tobias.</p>
    </article>
    <article class="review">
      <h4>CONTRACTOR</h4>
      <div class="meta">Nov 22, 2014 by Marcus</div>
      <svg class="stars" width="160" height="22" viewBox="0 0 160 22"><use href="#star" x="0"/><use href="#star" x="32"/><use href="#star" x="64"/><use href="#star" x="96"/><polygon points="138,0 140.9,6.9 148,7.6 142.6,12.3 144.2,19.5 138,15.8 131.8,19.5 133.4,12.3 128,7.6 135.1,6.9" fill="none" stroke="var(--star)" stroke-width="1.5"/><use href="#star" x="128" clip-path="url(#half)"/></svg>
      <p>Excellent and detailed professional, with installation of interactive projector, as well customizing install on white board. I highly recommend Tobias.</p>
    </article>
    <article class="review">
      <h4>LUMINOR BOARD "TUNE-UPS"</h4>
      <div class="meta">Nov 22, 2014 by Marcus</div>
      <svg class="stars" width="160" height="22" viewBox="0 0 160 22"><use href="#star" x="0"/><use href="#star" x="32"/><use href="#star" x="64"/><use href="#star" x="96"/><polygon points="138,0 140.9,6.9 148,7.6 142.6,12.3 144.2,19.5 138,15.8 131.8,19.5 133.4,12.3 128,7.6 135.1,6.9" fill="none" stroke="var(--star)" stroke-width="1.5"/><use href="#star" x="128" clip-path="url(#half)"/></svg>
      <p>Excellent and detailed professional, with installation of interactive projector, as well customizing install on white board. I highly recommend Tobias.</p>
    </article>
  </div>
  <div class="dots"><i class="off"></i><i></i><i></i><i></i></div>
</section>

<section class="news">
  <h2 class="section-title">NEWS</h2>
  <svg class="news-arrows" width="30" height="14" viewBox="0 0 30 14"><path d="M8 1 2 7l6 6M22 1l6 6-6 6" fill="none" stroke="#333" stroke-width="1.5"/></svg>
  <div class="date">DATE POSTED ON : DECEMBER 2014</div>
  <h2>Lorem Ipsum is simply dummy text of the printing and typesetting industry.</h2>
  <p class="excerpt">Lorem Ipsum has been the industry's standard dummy text ever since the 1500s, when an unknown printer took a galley of type and scrambled it to make a type specimen book. It has survived not only five centuries, but also the leap into electronic typesetting</p>
  <div class="ad-label">SPONSERED ADS</div>
  <div class="ad-slot" role="img" aria-label="Sponsored advertisement banner"></div>
</section>

<footer class="site-footer">
  <div class="social" aria-label="Social links"><i></i><i></i><i></i></div>
  <nav class="footer-nav"><span>HOME</span><span>|</span><span>SERVICES</span><span>|</span><span>CONTACT US</span><span>|</span><span>CUSTOMER REVIEWS</span></nav>
  <p class="copyright">© 2014 COMPANY NAME ,ALL RIGHTS RESERVED</p>
</footer>

</body>
</html>
```